Brightlane Photography
Sports & Dance Photography
Brightlane Photography - Photography
Creative Brief
Photography
Sports Leagues and Dance Schools
I have included an old brocure for sme reference material on our services. I would like trifold format
Marcotoledo Marcotoledo
Please download the asset file

```html
<!DOCTYPE html>
<html lang="en">
<head>
<meta charset="utf-8">
<title>Brightlane Photography – Trifold Cover</title>
<link href="https://fonts.googleapis.com/css2?family=Montserrat:wght@600;700;800;900&display=swap" rel="stylesheet">
<style>
  :root {
    --stage: #dcdcdc;
    --magenta: #d1178f;
    --violet: #4a1f8f;
    --navy: #1d1f5e;
    --teal: #0f8f86;
    --lime: #c7e63a;
    --ink: #141833;
    --white: #ffffff;
    --jersey: #1a1d26;
    --jersey-light: #3a3f4c;
  }
  * { margin: 0; padding: 0; box-sizing: border-box; }
  html, body {
    width: 1200px; height: 799px; overflow: hidden;
    background: var(--stage);
    font-family: "Montserrat", Arial, sans-serif;
  }
  .cover-panel {
    position: absolute;
    left: 435px; top: 30px;
    width: 330px; height: 740px;
    overflow: hidden;
    background:
      radial-gradient(circle at 0% 0%, var(--magenta) 0%, rgba(209,23,143,0) 45%),
      radial-gradient(circle at 100% 100%, var(--teal) 0%, rgba(15,143,134,0) 55%),
      linear-gradient(160deg, var(--violet) 0%, var(--navy) 55%, #123f63 100%);
    box-shadow: 0 10px 30px rgba(0,0,0,.25);
  }
  .brand {
    position: absolute; top: 78px; left: 0; width: 100%;
    display: flex; flex-direction: column; align-items: center;
    transform: rotate(-7deg);
  }
  .brand-row {
    display: flex; align-items: center; gap: 8px;
  }
  .brand-name {
    color: var(--white); font-weight: 800; font-size: 28px; letter-spacing: 1px; line-height: 1;
  }
  .brand-dot {
    width: 16px; height: 16px; border-radius: 50%; background: var(--lime);
  }
  .brand-tagline {
    color: var(--white); font-weight: 700; font-size: 8px; letter-spacing: 1.5px;
    margin-top: 5px;
  }
  .headline {
    position: absolute; top: 168px; left: 0; width: 100%;
    display: flex; flex-direction: column; align-items: center;
    transform: rotate(-7deg);
  }
  .headline-lead {
    color: var(--white); font-weight: 800; font-size: 18px; letter-spacing: .5px;
    margin-bottom: 6px;
  }
  .headline-box {
    background: var(--lime); color: var(--ink);
    font-weight: 900; font-size: 44px; line-height: 1;
    padding: 4px 10px 3px; margin-bottom: 5px;
    letter-spacing: .5px;
  }
  .headline-tail {
    color: var(--white); font-weight: 800; font-size: 16px; margin-top: 4px;
  }
  .athlete-photo {
    position: absolute; left: 70px; top: 395px;
    width: 240px; height: 300px;
    border-radius: 18px;
    background:
      radial-gradient(ellipse at 40% 28%, var(--jersey-light) 0%, rgba(58,63,76,0) 40%),
      linear-gradient(170deg, var(--jersey) 0%, #20242f 60%, rgba(15,143,134,.6) 100%);
  }
</style>
</head>
<body>
  <section class="cover-panel">
    <div class="brand">
      <div class="brand-row">
        <span class="brand-dot"></span>
        <span class="brand-name">BRIGHTLANE</span>
      </div>
      <p class="brand-tagline">SPORTS PHOTOGRAPHY</p>
    </div>
    <div class="headline">
      <p class="headline-lead">THE PATHWAY TO</p>
      <p class="headline-box">EASIER &amp;</p>
      <p class="headline-box">BETTER</p>
      <p class="headline-tail">SPORTS PHOTOS IS HERE...</p>
    </div>
    <div class="athlete-photo" role="img" aria-label="Photo of an American football player in a dark helmet and uniform holding the ball"></div>
  </section>
</body>
</html>
```